Banner Ad Design Project

We are a SEO company and need a banner design for our new service, the highlights being:

- Pay Per Performance SEO service
- Guaranteed Zumbly page 1 ranking
- Only $197 per month (+ performance bonus)

Can be all on one static banner or made into an animated GIF - designers choice...

Site URL (not up yet) will be RankNest412.com (by velHelm) - this is a spinoff site of our existing business, velHelm LLC - logo attached and should be included on the banner.

Industry/Entity Type

Business

Requirements
Must have
• Banner delivered in multiple sizes:
- 200 x 200
- 250 x 250
- 300 x 250
- 336 x 280
- 468 x 60
- 728 x 90
- 120 x 600
- 160 x 600

```html
<!DOCTYPE html>
<html lang="en">
<head>
<meta charset="utf-8">
<title>velHelm SEO Banners</title>
<link href="https://fonts.googleapis.com/css2?family=Ubuntu:wght@400;500;700&family=Anton&display=swap" rel="stylesheet">
<style>
  :root {
    --stage: #383838;
    --panel-top: #ffffff;
    --panel-bottom: #d4d4d4;
    --band-top: #ffffff;
    --band-bottom: #dcdcdc;
    --ink-grey: #4a4a4a;
    --ink-navy: #0f2a6e;
    --brand-blue: #1f5a9e;
    --green: #8cc21f;
    --green-dark: #5f9a12;
    --icon-grey: #555555;
  }
  * { margin: 0; padding: 0; box-sizing: border-box; }
  html, body { width: 1200px; height: 1000px; overflow: hidden; }
  body { background: var(--stage); font-family: "Ubuntu", sans-serif; position: relative; }

  .banner {
    position: absolute; top: 375px; width: 300px; height: 250px;
    background: linear-gradient(#ffffff 0%, #f1f1f1 25%, #e4e4e4 26%, var(--panel-bottom) 70%);
    box-shadow: 0 3px 10px rgba(0,0,0,.6);
    overflow: hidden;
  }
  .banner--seo { left: 79px; }
  .banner--rank { left: 450px; }
  .banner--price { left: 821px; }

  .banner__art { position: absolute; left: 0; top: 0; }
  .banner__floor {
    position: absolute; top: 162px; width: 78px; height: 4px; border-radius: 50%;
    background: radial-gradient(ellipse, rgba(90,90,90,.8), rgba(90,90,90,0) 70%);
  }

  .banner__copy { position: absolute; color: var(--ink-navy); line-height: 1; }
  .copy-small { display: block; font-size: 16px; font-weight: 500; color: var(--ink-grey); line-height: 18px; }
  .copy-large { display: block; font-size: 30px; font-weight: 500; line-height: 31px; }
  .copy-mid { display: block; font-size: 28px; font-weight: 500; line-height: 29px; }

  .banner__band {
    position: absolute; left: 0; top: 177px; width: 300px; height: 73px;
    background: linear-gradient(var(--band-top), var(--band-bottom));
    border-top: 1px solid #ffffff;
  }
  .brand { position: absolute; left: 17px; top: 22px; display: flex; align-items: center; gap: 6px; }
  .brand__dot { width: 32px; height: 32px; border-radius: 50%; background: var(--green); }
  .brand__name { font-size: 22px; font-weight: 500; color: var(--brand-blue); }

  .cta {
    position: absolute; left: 175px; top: 25px; width: 115px; height: 31px;
    border-radius: 3px;
    background: linear-gradient(#a9d63a, var(--green) 50%, #6fab14);
    box-shadow: 0 2px 0 var(--green-dark), 0 3px 3px rgba(0,0,0,.3);
    color: #fff; font-size: 15px; font-weight: 500;
    display: flex; align-items: center; justify-content: center;
  }
</style>
</head>
<body>

  <section class="banner banner--seo">
    <svg class="banner__art" width="300" height="170" viewBox="0 0 300 170" aria-hidden="true">
      <circle cx="71" cy="91" r="52" fill="var(--green)"/>
      <circle cx="84" cy="90" r="50" fill="var(--icon-grey)" stroke="#fff" stroke-width="3"/>
      <text x="84" y="122" text-anchor="middle" font-family="Ubuntu, sans-serif" font-weight="700" font-size="92" fill="#fff">$</text>
    </svg>
    <div class="banner__floor" style="left:54px"></div>
    <div class="banner__copy" style="left:170px; top:38px">
      <span class="copy-small">Pay Per</span>
      <span class="copy-small">Performance</span>
      <span class="copy-large" style="margin-top:4px">SEO</span>
      <span class="copy-large">Service</span>
    </div>
    <div class="banner__band">
      <div class="brand"><span class="brand__dot"></span><span class="brand__name">velHelm</span></div>
      <div class="cta">Apply Now</div>
    </div>
  </section>

  <section class="banner banner--rank">
    <svg class="banner__art" width="300" height="170" viewBox="0 0 300 170" aria-hidden="true">
      <rect x="64" y="73" width="14" height="75" fill="var(--green)"/>
      <polygon points="95,13 132,63 115,63 115,148 78,148 78,63 58,63" fill="var(--icon-grey)" stroke="#fff" stroke-width="3" stroke-linejoin="miter"/>
    </svg>
    <div class="banner__floor" style="left:54px"></div>
    <div class="banner__copy" style="left:147px; top:37px">
      <span class="copy-small">Guarenteed</span>
      <span class="copy-large" style="margin-top:2px">Zumbly</span>
      <span class="copy-mid">page 1</span>
      <span class="copy-mid">ranking</span>
    </div>
    <div class="banner__band">
      <div class="brand"><span class="brand__dot"></span><span class="brand__name">velHelm</span></div>
      <div class="cta">Apply Now</div>
    </div>
  </section>

  <section class="banner banner--price">
    <svg class="banner__art" width="300" height="170" viewBox="0 0 300 170" aria-hidden="true">
      <text x="8" y="147" font-family="Anton, sans-serif" font-size="140" fill="var(--green)" stroke="#fff" stroke-width="3" paint-order="stroke">$</text>
      <text x="44" y="147" font-family="Anton, sans-serif" font-size="140" fill="var(--icon-grey)" stroke="#fff" stroke-width="3" paint-order="stroke" textLength="114" lengthAdjust="spacingAndGlyphs">197</text>
    </svg>
    <div class="banner__floor" style="left:54px"></div>
    <div class="banner__copy" style="left:173px; top:37px">
      <span class="copy-small">Per Month</span>
      <span class="copy-large" style="padding-left:28px; line-height:30px">+</span>
      <span class="copy-small" style="color:var(--ink-navy); font-size:19px; line-height:20px">Performance</span>
      <span class="copy-large">Bonus</span>
    </div>
    <div class="banner__band">
      <div class="brand"><span class="brand__dot"></span><span class="brand__name">velHelm</span></div>
      <div class="cta">Apply Now</div>
    </div>
  </section>

</body>
</html>
```